A building General Contractor is looking for a business card design

I need a business card designed. The company "Stoneridge Framing Contractors" is a general contractor for commercial buildings and pre-engineered metal buildings.

```html
<!DOCTYPE html>
<html lang="en">
<head>
<meta charset="utf-8">
<title>Stoneridge Framing Contractors – Business Card</title>
<link href="https://fonts.googleapis.com/css2?family=Montserrat:wght@400;500;700;800&display=swap" rel="stylesheet">
<style>
  :root {
    --canvas: #d9d9db;
    --card-black: #121212;
    --card-black-soft: #1e1e1e;
    --paper-white: #ffffff;
    --text-light: #f2f2f2;
    --text-muted: #cfcfcf;
    --rule: #8a8a8a;
    --ink: #111111;
  }
  * { box-sizing: border-box; margin: 0; padding: 0; }
  html, body {
    width: 1200px; height: 900px; overflow: hidden;
    background: var(--canvas);
    font-family: "Montserrat", sans-serif;
  }
  .sheet {
    position: relative; width: 1200px; height: 900px;
    display: flex; flex-direction: column; align-items: center; justify-content: center; gap: 36px;
  }
  .card {
    position: relative; width: 720px; height: 400px;
    border-radius: 26px; overflow: hidden;
    background: var(--card-black);
    box-shadow: 0 10px 30px rgba(0,0,0,.25);
  }

  /* Back side */
  .card-back .pattern-area {
    position: absolute; inset: 0;
    background: linear-gradient(120deg, #2a2a2a 0%, #0d0d0d 45%, #1b1b1b 70%, #090909 100%);
  }
  .card-back .corner-name {
    position: absolute; top: 54px; right: 48px;
    display: flex; align-items: center; gap: 8px;
    font-weight: 700; font-size: 13px; letter-spacing: .08em;
    color: var(--text-light); text-transform: uppercase;
  }
  .corner-name .mark-square { width: 10px; height: 10px; background: var(--text-light); }

  /* Front side */
  .card-front .white-sweep { position: absolute; inset: 0; width: 100%; height: 100%; }
  .card-front .brand-name {
    position: absolute; right: 44px; top: 110px; width: 300px;
    font-weight: 800; font-size: 34px; line-height: 1.08;
    color: var(--ink); text-transform: uppercase; letter-spacing: .02em;
    text-align: left;
  }
  .contact-block {
    position: absolute; left: 50px; top: 108px; width: 290px;
    color: var(--text-light);
  }
  .person-name {
    font-weight: 800; font-size: 26px; letter-spacing: .06em; text-transform: uppercase;
  }
  .person-role { font-size: 14px; color: var(--text-muted); margin-top: 2px; }
  .rule { height: 1px; background: var(--rule); margin: 14px 0; width: 100%; }
  .address { font-size: 14px; line-height: 1.35; color: var(--text-muted); }
  .contact-list { list-style: none; }
  .contact-list li {
    display: flex; align-items: center; gap: 10px;
    font-size: 14px; line-height: 1.9; color: var(--text-muted);
  }
  .contact-list svg { width: 13px; height: 13px; flex: none; fill: var(--text-light); }
</style>
</head>
<body>
<main class="sheet">

  <section class="card card-back" aria-label="Card back">
    <div class="pattern-area" role="img" aria-label="Glossy repeating brand pattern on black"></div>
    <div class="corner-name"><span class="mark-square"></span>Stoneridge</div>
  </section>

  <section class="card card-front" aria-label="Card front">
    <svg class="white-sweep" viewBox="0 0 720 400" preserveAspectRatio="none" aria-hidden="true">
      <path d="M400 0 H720 V330 C620 335 520 320 455 285 C380 240 340 150 360 60 C365 35 380 12 400 0 Z" fill="#ffffff"/>
      <path d="M470 318 C560 352 650 358 720 350 V362 C640 372 545 362 470 318 Z" fill="#ffffff"/>
    </svg>

    <div class="brand-name">Stoneridge Framing Contractors</div>

    <div class="contact-block">
      <h1 class="person-name">Daniel Reyes</h1>
      <p class="person-role">Founder</p>
      <div class="rule"></div>
      <p class="address">418 Quarry Lane<br>Garner, NC 27529</p>
      <div class="rule"></div>
      <ul class="contact-list">
        <li>
          <svg viewBox="0 0 24 24"><path d="M6.6 10.8a15.1 15.1 0 0 0 6.6 6.6l2.2-2.2a1 1 0 0 1 1-.25 11.4 11.4 0 0 0 3.6.57 1 1 0 0 1 1 1V20a1 1 0 0 1-1 1A17 17 0 0 1 3 4a1 1 0 0 1 1-1h3.5a1 1 0 0 1 1 1c0 1.25.2 2.45.57 3.6a1 1 0 0 1-.25 1z"/></svg>
          919-555-0148
        </li>
        <li>
          <svg viewBox="0 0 24 24"><path d="M2 5h20v14H2z M2 5l10 8 10-8" fill="none" stroke="#f2f2f2" stroke-width="2"/></svg>
          info@yourmail.com
        </li>
        <li>
          <svg viewBox="0 0 24 24"><circle cx="12" cy="12" r="9" fill="none" stroke="#f2f2f2" stroke-width="2"/><path d="M3 12h18M12 3c3 3 3 15 0 18M12 3c-3 3-3 15 0 18" fill="none" stroke="#f2f2f2" stroke-width="1.5"/></svg>
          www.website.com
        </li>
      </ul>
    </div>
  </section>

</main>
</body>
</html>
```